Brochure Design Project

Color brochure with text, graphics, and photos. (I will provide the text). 4 pages of 8 1/2 X 11". This is a brochure about dental implants.
Attached is the text and logo for the brochure.

See new parameters and information on the brochure project.

Included in the brochure is our address: Briar Ridge Dental Care, 418 North Cedar Avenue, Briar Ridge, PA 17943.  717-829-4617.  www.briarridgedentalcare.example.

Martin R. Pike, D.M.D., M.A.G.D., F.I.C.O.I. (Attached is photo for brochure)file://localhost/Users/mrpdmd7/Pictures/iPhoto%20Library/Masters/2003/Office%20Pictures/Dr.%20Pike%202.jpg

Target Market(s)

Adults, primarily senior adults.

Industry/Entity Type

Dental

```html
<!DOCTYPE html>
<html lang="en">
<head>
<meta charset="utf-8">
<title>The Magic Of Dental Implants – Brochure</title>
<link rel="stylesheet" href="https://fonts.googleapis.com/css2?family=Open+Sans:ital,wght@0,400;0,600;0,700;1,400&family=Tinos:wght@400;700&display=swap">
<style>
:root{
  --blue-deep:#24479a;
  --blue-mid:#3471c9;
  --blue-light:#6fa3e6;
  --blue-ink:#1f4fb0;
  --sky:#e9f1fb;
  --white:#ffffff;
  --ink:#1c1c1c;
  --rule:#9fb6d8;
  --photo-green:#6d8f3c;
  --photo-tan:#b9905c;
  --photo-skin:#b97c5d;
  --photo-pink:#d98b8f;
  --tooth:#f3efe6;
}
*{margin:0;padding:0;box-sizing:border-box}
html,body{width:828px;height:1200px;overflow:hidden;background:var(--white)}
body{position:relative;font-family:"Tinos","Times New Roman",serif;color:var(--ink)}
.abs{position:absolute}

/* outside trifold */
.panel{position:absolute;top:69px;height:538px;overflow:hidden}
.panel-features{left:79px;width:243px;background:linear-gradient(180deg,var(--blue-mid) 0%,#2f62b8 60%,var(--blue-deep) 100%)}
.panel-benefits{left:322px;width:200px;background:linear-gradient(180deg,#ffffff 0%,var(--sky) 100%)}
.panel-cover{left:522px;width:245px;background:linear-gradient(180deg,#2a5cb4 0%,var(--blue-mid) 45%,var(--blue-light) 100%)}

.features-title{top:14px;left:0;width:243px;text-align:center;font:700 17px/1.15 "Open Sans",sans-serif;color:var(--white)}
.feature{position:absolute;left:10px;width:225px;display:flex;gap:8px;align-items:center}
.feature-num{flex:none;width:32px;height:32px;border:2px solid var(--white);border-radius:50%;color:var(--white);font:400 22px/28px "Open Sans",sans-serif;text-align:center}
.feature-text{font:400 9px/1.3 "Open Sans",sans-serif;color:var(--white)}
.photo{position:absolute}
.photo-wildlife{left:67px;top:115px;width:137px;height:102px;background:linear-gradient(180deg,#7fb0d8 0%,var(--photo-green) 45%,var(--photo-tan) 100%);border:2px solid var(--white)}
.photo-friends{left:21px;top:304px;width:208px;height:74px;background:linear-gradient(90deg,#7b4a35,var(--photo-skin) 40%,#e2b48d 70%,#8a5a40)}

.benefits-head{top:12px;left:10px;width:185px;font:700 10px/1.25 "Open Sans",sans-serif;color:var(--blue-ink)}
.benefits-body{left:10px;width:182px;font:400 10.5px/1.22 "Tinos",serif}
.photo-smile{left:9px;top:161px;width:180px;height:72px;background:linear-gradient(90deg,#dfe8f2 0%,#e8d2c2 55%,#f2f4f7 100%)}
.practice-mark{left:52px;top:336px;width:96px;height:56px;display:flex;flex-direction:column;align-items:center;gap:4px}
.mark-dot{width:26px;height:26px;border-radius:50%;background:var(--blue-ink)}
.mark-name{font:700 9px/1.1 "Open Sans",sans-serif;color:var(--blue-ink);text-align:center}
.contacts-head{top:408px;left:0;font:400 21px/1 "Open Sans",sans-serif;color:var(--blue-mid);padding-left:1px}
.contacts-body{top:437px;left:1px;width:196px;font:400 9.5px/1.25 "Open Sans",sans-serif;color:#4f6ea8}
.contacts-phone{font-size:16px;line-height:1.1}

.cover-mark{left:90px;top:12px;width:66px;height:66px;border-radius:50%;background:var(--white);display:flex;align-items:center;justify-content:center;text-align:center;font:700 8px/1.15 "Open Sans",sans-serif;color:var(--blue-ink);padding:6px}
.cover-title{top:98px;left:18px;width:230px;font:700 27px/1.18 "Tinos",serif;color:var(--white)}
.cover-ghost{top:160px;left:40px;font:700 44px/1 "Tinos",serif;color:rgba(255,255,255,.13);transform:rotate(-28deg);white-space:nowrap}
.art-implants{left:82px;top:345px;width:150px;height:135px;background:linear-gradient(180deg,#f1f1ee 0%,#d6d8dc 38%,var(--photo-pink) 62%,var(--tooth) 100%);border-radius:24px}

/* inside spread */
.spread-title{top:636px;left:0;width:828px;text-align:center;font:600 26px/1.2 "Open Sans",sans-serif;color:var(--blue-ink)}
.spread{position:absolute;left:79px;top:683px;width:688px;height:474px;overflow:hidden;background:linear-gradient(180deg,#ffffff 0%,var(--sky) 100%)}
.danger{position:absolute;border:1px solid var(--rule);background:rgba(255,255,255,.85);padding:6px 7px 7px}
.danger-head{display:flex;gap:6px;align-items:flex-start;margin-bottom:5px}
.danger-num{flex:none;width:30px;height:30px;border:2px solid var(--blue-ink);border-radius:50%;color:var(--blue-ink);font:400 22px/26px "Open Sans",sans-serif;text-align:center;background:var(--white);margin-top:-2px}
.danger-title{font:400 10px/1.2 "Tinos",serif;color:var(--blue-ink)}
.danger-text{font:400 9.5px/1.17 "Tinos",serif;text-align:justify}
.danger-one{left:24px;top:18px;width:219px}
.danger-two{left:252px;top:156px;width:178px}
.danger-three{left:470px;top:21px;width:177px}
.photo-mouth{left:24px;top:239px;width:191px;height:110px;background:radial-gradient(ellipse at 50% 55%,var(--tooth) 0%,#d9a2a0 30%,#9a3a3e 65%,#5b1e22 100%)}
.art-implant-section{left:256px;top:14px;width:176px;height:117px;background:linear-gradient(180deg,#e6b7b0 0%,#d89a93 35%,#f4efe6 65%,#ffffff 100%)}
.services{left:478px;top:318px;width:200px;display:grid;grid-template-columns:max-content max-content;gap:3px 12px;font:400 9px/1.25 "Open Sans",sans-serif;color:var(--white)}
.services li{list-style:none;white-space:nowrap}
.services li::before{content:"• "}
.tagline{left:470px;top:394px;width:200px;text-align:center;font:italic 400 18px/1.25 "Open Sans",sans-serif;color:var(--white);letter-spacing:.5px}
.tagline .big{font-size:24px;letter-spacing:1px}
</style>
</head>
<body>

<!-- outside trifold -->
<section class="panel panel-features">
  <h2 class="abs features-title">The Magic Of<br>Dental Implants</h2>
  <div class="feature" style="top:58px"><span class="feature-num">1</span><p class="feature-text">Duis aute irure dolor in reprehenderit in voluptate velit esse cillum dolore eu fugiat nulla pariatur. Excepteur sint</p></div>
  <div class="photo photo-wildlife" role="img" aria-label="Photo of antelopes grazing in green grassland"></div>
  <div class="feature" style="top:232px"><span class="feature-num">2</span><p class="feature-text">Duis aute irure dolor in reprehenderit in voluptate velit esse cillum dolore eu fugiat nulla pariatur. Excepteur sint</p></div>
  <div class="photo photo-friends" role="img" aria-label="Photo of a group of smiling women"></div>
  <div class="feature" style="top:396px"><span class="feature-num">3</span><p class="feature-text">Duis aute irure dolor in reprehenderit in voluptate velit esse cillum dolore eu fugiat nulla pariatur. Excepteur sint</p></div>
</section>

<section class="panel panel-benefits">
  <h3 class="abs benefits-head">What are the Benefits of<br>Dental Implants?</h3>
  <p class="abs benefits-body" style="top:46px">Here is a list of just a few of the benefits:</p>
  <p class="abs benefits-body" style="top:73px">Prevents Bone Loss – By preventing bone loss that normally occurs with the loss of teeth, the facial structure remains intact. This is especially important when all of the teeth are missing because your face has a tendency to collapse if implants are not placed to preserve the bone.</p>
  <div class="photo photo-smile" role="img" aria-label="Photo of a smiling senior woman"></div>
  <p class="abs benefits-body" style="top:248px">Improves overall oral health and decreases the risk of oral cancer and heart disease. It is much easier to care for implants versus the care of dentures. Your chances of bacteria build up decreases when you have implants.</p>
  <div class="abs practice-mark"><span class="mark-dot"></span><span class="mark-name">Briar Ridge Dental Care</span></div>
  <svg class="abs" style="left:0;top:470px" width="200" height="68" viewBox="0 0 200 68" aria-hidden="true">
    <path d="M0 40 C60 20 130 18 200 30 L200 68 L0 68Z" fill="#7aa8e4"/>
    <path d="M0 50 C70 34 140 34 200 42 L200 68 L0 68Z" fill="#2f62b8"/>
  </svg>
  <h3 class="abs contacts-head">Contacts</h3>
  <p class="abs contacts-body">Briar Ridge Dental Care, 418 North Cedar Avenue, Briar Ridge, PA 17943.<br><span class="contacts-phone">(717)-829-4617</span><br>www.briarridgedentalcare.example</p>
</section>

<section class="panel panel-cover">
  <svg class="abs" style="left:0;top:0" width="245" height="538" viewBox="0 0 245 538" aria-hidden="true">
    <path d="M245 210 C150 240 40 300 0 400 L0 538 L245 538Z" fill="#ffffff" opacity=".85"/>
    <path d="M245 250 C160 275 60 330 0 420 L0 538 L245 538Z" fill="#d6e5f8"/>
    <path d="M0 505 C80 485 170 480 245 490 L245 538 L0 538Z" fill="#3f78cf"/>
  </svg>
  <span class="abs cover-ghost" aria-hidden="true">Magic Of The</span>
  <div class="abs cover-mark">Briar Ridge Dental Care</div>
  <h1 class="abs cover-title">The Magic Of<br>Dental Implants</h1>
  <div class="abs art-implants" role="img" aria-label="Illustration of upper and lower dentures on implant posts"></div>
</section>

<!-- inside spread -->
<h2 class="abs spread-title">3 Dangers of Tooth Loss and Poor Fitting Dentures</h2>
<section class="spread">
  <svg class="abs" style="left:0;top:0" width="688" height="474" viewBox="0 0 688 474" aria-hidden="true">
    <path d="M0 360 C200 300 420 260 688 180 L688 474 L0 474Z" fill="#cfe0f6" opacity=".6"/>
    <path d="M440 474 C470 380 560 300 688 250 L688 474Z" fill="#4a82d6"/>
    <path d="M0 430 C220 400 430 360 688 300 L688 474 L0 474Z" fill="#3a70c8"/>
    <path d="M0 455 C250 430 470 400 688 370 L688 474 L0 474Z" fill="#24479a"/>
  </svg>

  <article class="danger danger-one">
    <div class="danger-head"><span class="danger-num">1</span><h4 class="danger-title">Danger #1: Bone Loss Makes You Look Older Quicker</h4></div>
    <p class="danger-text">Dental Implants assist you in looking and feeling younger, because they prevent bone loss. By preventing bone loss that would normally occur with the loss of teeth, your facial structure remains normal and intact. The chances of wrinkling and aging before your time is less likely to happen. In other words, every day that you continue to wear dentures you are experiencing bone loss, which makes you look much older than you have to.</p>
  </article>
  <div class="photo photo-mouth" role="img" aria-label="Close-up photo of a mouth with missing teeth"></div>

  <div class="photo art-implant-section" role="img" aria-label="Illustration of a dental implant set in the jawbone between natural teeth"></div>
  <article class="danger danger-two">
    <div class="danger-head"><span class="danger-num">2</span><h4 class="danger-title">Danger #2: Dentures Increase Your Risk of Heart Disease and Oral Cancer</h4></div>
    <p class="danger-text">While tooth loss may seem like a small problem compared with other health and fitness issues, it is often the first sign of bigger health problems for many people and can put them at higher risk for heart disease and oral cancer. When dentures don't fit properly, or are not removed daily, it can lead to bone disease and oral cancer. The National Oral Health Council reports that there will be approximately 30,000 new cases of oral cancer this year alone. Heart disease has been linked to gum disease. When dentures do not fit correctly, you have a higher chance of oral problems. You must be aware of these concerns because dentures can cause more problems than just discomfort and a poor smile.</p>
  </article>

  <article class="danger danger-three">
    <div class="danger-head"><span class="danger-num">3</span><h4 class="danger-title">Danger #3: Dentures May Reduce Your Life Span</h4></div>
    <p class="danger-text">It's True! Many people with poor fitting dentures or multiple missing back teeth live up to 10 years less. This is due to poor eating habits and stomach problems. Denture wearers tend to eat more processed foods and experience other health problems related to poor eating habits. People today now have alternatives to dentures, and the best solution is dental implants. People who get dental implants can finally eat the healthy foods they have been missing such as; apples, fresh vegetables, corn on the cob, and even steak!</p>
  </article>

  <ul class="abs services">
    <li>Asset Allocation</li><li>Income Taxes</li>
    <li>Asset Accumulation</li><li>Disability</li>
    <li>Estate Planning</li><li>Education Planning</li>
  </ul>
  <p class="abs tagline">YOUR PARTNER<br><span class="big">FOR SUCCESS</span></p>
</section>

</body>
</html>
```